Lift Your Standing - Search Engine Website

I am launching an SEO website and I am looking to have the site designed. There are a total of 8-10 pages that will need to be designed. I am providing 2 pages off the bat and will work with a designer once these 2 pages are complete. I have never posted a contest for website design (only logos, brochures, etc) so please let me know if there is anything you need from me. I am uploading 2 versions of our logo - a horizontal and a vertical version. I was thinking of getting these rendered in 3d, but I am just going with these for now. I am hoping to complete all work in 10 days, so hopefully the right design for the 1st 2 pages are submitted promptly.

We provide search engine optomization tools and backlinking tools. We provide free research tools as well as cost effective packages for SEO.

I am including 2 word files that have info about the home page and keyword summary page. Additional pages will include: Keyword Research Summary, The Slate, Reports, etc.

I am also uploading a zip file that has some examples of home pages that I like. None of them are exactly what I am looking for, but they have certain elements that I like.

I am looking for a clean design and stands out and has good use of color.

Link to instructions files (2...more will be uploaded as first 2 pages are finalized): https://www.filecrate-example.net/sh/k4m2w7z9q3v1b8x/tRn_p-7ab2
Updates

Forgot to include our logos. Here is a drop box link to the logos: 

https://www.filecrate-example.net/sh/93jd2kq7zt5wmvp/8h2PLmz4Xe

Target Market(s)

big and small businesses, resellers

Industry/Entity Type

Seo

Requirements
Must have
• see attached MS Word files for details about requirements.

```html
<!DOCTYPE html>
<html lang="en">
<head>
<meta charset="utf-8">
<title>Lift Your Standing</title>
<link href="https://fonts.googleapis.com/css2?family=Roboto+Condensed:wght@400;700&family=PT+Sans:wght@400;700&display=swap" rel="stylesheet">
<style>
:root{
  --orange:#f7941d;
  --orange-light:#fbb040;
  --orange-deep:#f26f21;
  --blue:#1f5fb0;
  --blue-bright:#2a86d8;
  --ink:#333;
  --grey-text:#555;
  --maroon:#8b1a1a;
  --footer:#4b4b4b;
  --footer-text:#d8d8d8;
  --white:#fff;
}
*{margin:0;padding:0;box-sizing:border-box}
html,body{width:1011px;height:1200px;overflow:hidden;background:#fff}
body{font-family:"PT Sans",sans-serif;color:var(--ink)}
.page{position:relative;width:1011px;height:1200px;overflow:hidden;background:linear-gradient(#fff 0,#fff 640px,#f1f1f1 680px,#fff 720px)}
.abs{position:absolute}
.cond{font-family:"Roboto Condensed",sans-serif}

/* header */
.brand{left:97px;top:17px;font-family:"Roboto Condensed",sans-serif;font-weight:700;font-size:38px;color:var(--blue);letter-spacing:.5px;display:flex;align-items:center;gap:8px}
.brand-dot{width:14px;height:14px;border-radius:50%;background:var(--orange)}
.tagline{left:100px;top:69px;font-size:11px;color:#222}
.invite{left:687px;top:34px;width:192px;height:28px;background:linear-gradient(#5b7fc4,#3b5ea8);border:1px solid #2d4a8a;color:#fff;font-size:11px;display:flex;align-items:center}
.invite .sq{width:28px;height:100%;background:#2f4f94;border-right:1px solid #6a88c8}
.invite span{padding-left:16px}

/* nav */
.nav{left:0;top:97px;width:1011px;height:45px;background:linear-gradient(var(--orange-light),var(--orange-deep));border-bottom:2px solid #fff}
.nav ul{list-style:none;position:absolute;left:97px;top:0;height:45px;display:flex}
.nav li{font-family:"Roboto Condensed",sans-serif;font-weight:700;font-size:13px;color:#fff;height:45px;line-height:45px;padding:0 11px;border-right:1px solid rgba(255,255,255,.35)}
.nav li.active{background:var(--blue);width:78px;text-align:center;padding:0;border-right:none}
.nav li:last-child{border-right:none}
.pill{top:9px;height:27px;border-radius:7px;background:linear-gradient(#ffe066,#f2b705);border:2px solid #fff3a8;box-shadow:0 2px 3px rgba(0,0,0,.25);font-family:"Roboto Condensed",sans-serif;font-weight:700;font-size:14px;color:#fff;text-align:center;line-height:23px}

/* hero */
.hero{left:0;top:142px;width:1011px;height:389px;background:radial-gradient(ellipse at 50% 40%,#fbab3c 0,#f7931e 60%,#f47b20 100%);overflow:hidden}
.hero h1{position:absolute;left:126px;top:52px;font-family:"Roboto Condensed",sans-serif;font-weight:700;font-size:24px;line-height:32px;color:#fff}
.hero ul{list-style:none;position:absolute;left:140px;top:142px}
.hero li{font-family:"Roboto Condensed",sans-serif;font-weight:700;font-size:12px;color:#fff;height:30.5px;padding-left:12px;position:relative}
.hero li::before{content:"›";position:absolute;left:0;top:-2px;font-size:13px}
.btn-dark{height:47px;border-radius:4px;background:linear-gradient(#4a4a4a,#0d0d0d);border:2px solid #fff;box-shadow:2px 3px 4px rgba(0,0,0,.35);font-family:"Roboto Condensed",sans-serif;font-weight:700;font-size:19px;color:#fff;text-align:center;line-height:43px}
.btn-dark.gold{color:#f7c118}
.dots{left:150px;top:340px;display:flex;gap:5px}
.dots i{width:13px;height:13px;border-radius:50%;background:#fff;border:1px solid #ddd}
.dots i.on{background:#f2c40f}
.research-title{left:624px;top:52px;font-family:"Roboto Condensed",sans-serif;font-weight:700;font-size:23px;color:#fff}
.field{left:628px;width:237px;height:32px;background:#fff;border:1px solid #e3d3c0;border-radius:3px;font-size:9.5px;color:#666;padding-left:11px;line-height:30px}
.research-note{left:633px;top:323px;width:230px;font-size:9.5px;line-height:15px;color:#fff}

/* feature strip */
.strip-band{left:0;top:531px;width:1011px;height:64px;background:#e6e6e6}
.strip{left:97px;top:531px;width:809px;height:108px;background:#fff;border:1px solid #ccc;border-top:none;box-shadow:0 4px 6px rgba(0,0,0,.12)}
.badge{width:80px;height:80px;border-radius:50%;border:3px solid var(--orange)}
.feat{font-family:"Roboto Condensed",sans-serif;font-weight:700;color:#555}

/* content */
.content{left:97px;top:691px;width:809px;height:364px;background:#fff;border:1px solid #ccc;border-bottom:none;border-radius:3px 3px 0 0}
.section-title{font-family:"Roboto Condensed",sans-serif;font-weight:700;font-size:19px;color:#555}
.photo{width:91px;height:89px;border-radius:4px;background:linear-gradient(#a08a78,#4a3a30);box-shadow:0 1px 3px rgba(0,0,0,.4)}
.post-title{font-size:12px;color:var(--maroon)}
.post-body{width:350px;font-size:9.5px;line-height:13.5px;color:#222}
.shares{display:flex;gap:6px;align-items:center}
.sbtn{height:16px;border:1px solid #b8c7d8;border-radius:2px;background:linear-gradient(#fff,#e6edf5);font-size:9px;color:#2c5b9a;padding:0 6px;line-height:14px}
.count{height:16px;border:1px solid #c7c7c7;background:#fff;font-size:9px;line-height:14px;padding:0 6px;color:#333}
.btn-blue{left:414px;top:981px;width:130px;height:28px;border-radius:3px;background:linear-gradient(var(--blue-bright),#1a5fae);font-family:"Roboto Condensed",sans-serif;font-weight:700;font-size:13px;color:#fff;text-align:center;line-height:28px}
.video{left:622px;top:751px;width:260px;height:145px;background:linear-gradient(135deg,#d9d9d9,#a7a7a7);border:2px solid #111}
.video-bar{left:624px;top:885px;width:256px;height:9px;background:#111}
.video-text{left:625px;top:908px;width:260px;font-size:9.5px;line-height:15px;color:#222}
.btn-orange{left:783px;top:977px;width:97px;height:31px;border-radius:7px;background:linear-gradient(#fba040,#f07a1a);font-size:10.5px;color:#fff;text-align:center;line-height:31px}

/* footer */
.footer{left:0;top:1055px;width:1011px;height:145px;background:var(--footer);border-top:3px solid #3a3a3a}
.fcol{top:23px}
.fcol h3{font-weight:400;font-size:12px;color:#e8e8e8;margin-bottom:9px}
.fcol li{list-style:none;font-size:9.5px;color:var(--footer-text);height:18.3px;padding-left:3px}
.social{left:782px;top:21px;display:flex;gap:13px}
.social i{width:20px;height:20px;border-radius:3px;display:block}
.copy{left:690px;top:63px;font-size:9.5px;color:var(--footer-text)}
.x2{left:893px;top:85px;font-size:9.5px;color:var(--footer-text)}
</style>
</head>
<body>
<div class="page">

  <header>
    <div class="abs brand"><span class="brand-dot"></span>LiftYourStanding.net</div>
    <p class="abs tagline">Lift Your Search Engine Standing Using Legal Back Linking Techniques.</p>
    <div class="abs invite"><div class="sq"></div><span>Invite Friends Via Friendbook</span></div>
  </header>

  <nav class="abs nav">
    <ul>
      <li class="active">Home</li>
      <li>About Us</li>
      <li>Services</li>
      <li>Features</li>
      <li>Resources</li>
      <li>Free Trial</li>
      <li>FAQ</li>
      <li>Contact Us</li>
    </ul>
    <div class="abs pill" style="left:714px;width:75px">SIGNUP</div>
    <div class="abs pill" style="left:803px;width:74px">LOGIN</div>
  </nav>

  <section class="abs hero">
    <svg class="abs" style="left:0;top:0" width="1011" height="389" aria-hidden="true">
      <path d="M380 0 C 480 120, 470 280, 380 389" stroke="rgba(255,255,255,.12)" stroke-width="2" fill="none"/>
      <path d="M560 0 C 640 140, 640 260, 600 389" stroke="rgba(255,255,255,.12)" stroke-width="2" fill="none"/>
      <path d="M880 0 C 980 140, 970 270, 940 389" stroke="rgba(255,255,255,.12)" stroke-width="2" fill="none"/>
    </svg>
    <h1>Lift Your Search Engine Standing Using<br>Legal Back Linking Techniques</h1>
    <ul>
      <li>Lift Standing of your Business Webpage, VidStream Video, Social Media Page &amp; Blog</li>
      <li>Lift Pages from various websites</li>
      <li>Snapshots and Progress Reports of your search engine rankings</li>
    </ul>
    <div class="abs btn-dark gold" style="left:145px;top:246px;width:140px">BUY NOW</div>
    <div class="abs btn-dark" style="left:305px;top:246px;width:141px">FREE TRIAL</div>
    <div class="abs dots"><i></i><i></i><i class="on"></i></div>

    <h2 class="abs research-title">FREE KEYWORD RESEARCH</h2>
    <div class="abs field" style="top:108px">Enter Your Url Here</div>
    <div class="abs field" style="top:160px">Enter Your Keywords Here</div>
    <div class="abs field" style="top:211px">Type in Competitior Url Here</div>
    <div class="abs btn-dark" style="left:721px;top:263px;width:141px">SEARCH</div>
    <p class="abs research-note">Current Search Engine Ranking, Research Keyword popularity and competitiveness, See what your competitors are doing!</p>
  </section>

  <div class="abs strip-band"></div>
  <section class="abs strip">
    <div class="abs badge" role="img" aria-label="Free trial badge illustration" style="left:31px;top:13px;background:radial-gradient(#fff6d0,#f2b12a)"></div>
    <div class="abs feat" style="left:123px;top:27px;font-size:14px">FREE</div>
    <div class="abs feat" style="left:123px;top:44px;font-size:24px">TRIAL</div>
    <div class="abs badge" role="img" aria-label="Blue question mark illustration" style="left:288px;top:13px;background:radial-gradient(#d8ecfb,#7fb7e6)"></div>
    <div class="abs feat" style="left:380px;top:28px;font-size:16px">WHY LIFT</div>
    <div class="abs feat" style="left:380px;top:57px;font-size:16px">YOUR STANDING</div>
    <div class="abs badge" role="img" aria-label="Blue SEO puzzle piece illustration" style="left:580px;top:13px;background:radial-gradient(#4aa0ea,#1466c0)"></div>
    <div class="abs feat" style="left:672px;top:28px;font-size:16px">SEO</div>
    <div class="abs feat" style="left:672px;top:56px;font-size:18px">BASICS</div>
  </section>

  <main class="abs content"></main>
  <h2 class="abs section-title" style="left:113px;top:706px">Recent Blog</h2>

  <article>
    <div class="abs photo" role="img" aria-label="Author portrait photo" style="left:115px;top:750px"></div>
    <h3 class="abs post-title" style="left:219px;top:745px;font-weight:400">Lorem Ipsum has been the industry's standard dummy text.</h3>
    <p class="abs post-body" style="left:221px;top:767px">E-Commerce is a major progress in technology that has changed the way in which the customers now purchase , products and the services.E-Commerce is a major progress in technology that has changed the way in which the customers now</p>
    <div class="abs shares" style="left:224px;top:824px"><span class="sbtn">Like</span><span class="count">0</span><span class="sbtn">Share</span><span class="count">7</span><span class="sbtn">+1</span></div>
  </article>
  <article>
    <div class="abs photo" role="img" aria-label="Author portrait photo" style="left:115px;top:869px"></div>
    <h3 class="abs post-title" style="left:219px;top:864px;font-weight:400">Lorem Ipsum has been the industry's standard dummy text.</h3>
    <p class="abs post-body" style="left:221px;top:886px">E-Commerce is a major progress in technology that has changed the way in which the customers now purchase , products and the services.E-Commerce is a major progress in technology that has changed the way in which the customers now</p>
    <div class="abs shares" style="left:224px;top:943px"><span class="sbtn">Like</span><span class="count">0</span><span class="sbtn">Share</span><span class="count">7</span><span class="sbtn">+1</span></div>
  </article>
  <div class="abs btn-blue">More Post</div>

  <h2 class="abs section-title" style="left:619px;top:706px">Featured Video</h2>
  <div class="abs video" role="img" aria-label="Video still of search engine optimization words under a magnifier"></div>
  <svg class="abs" style="left:734px;top:801px" width="34" height="34" aria-hidden="true">
    <circle cx="17" cy="17" r="15" fill="rgba(90,90,90,.8)" stroke="#fff" stroke-width="2"/>
    <path d="M13 10 L24 17 L13 24 Z" fill="#fff"/>
  </svg>
  <div class="abs video-bar"></div>
  <p class="abs video-text">Uenim ad minim veniam, quis laboris nisi utaliquip ex irurdolor into Uenim ad minim veniam, quis nostrud Uenim ad minim veniam, quis laboris nisi utaliquip ex irurdolor into Uenim adminim veniam, quis nostrud</p>
  <div class="abs btn-orange">View More...</div>

  <footer class="abs footer">
    <div class="abs fcol" style="left:94px"><h3>Company</h3><ul><li>About Us</li><li>Why Lift Your Standing</li><li>Affiliate Program</li><li>Tips To Using Our System</li><li>FAQ</li></ul></div>
    <div class="abs fcol" style="left:304px"><h3>Services</h3><ul><li>Link Building</li><li>Local SEO</li><li>Free Trial</li><li>Free Keyword Analysis Tools</li><li>VidStream Video Marketing</li></ul></div>
    <div class="abs fcol" style="left:494px"><h3>SEO</h3><ul><li>SEO Basics</li><li>SEO Tips</li><li>On Page SEO</li><li>Off Page SEO</li></ul></div>
    <div class="abs social"><i style="background:#3b5ea8"></i><i style="background:#2fa0dc"></i><i style="background:#1a7bb8"></i><i style="background:#f58a1f"></i></div>
    <p class="abs copy">© 2013 liftyourstanding.net. All rights reserved.</p>
    <p class="abs x2">x2</p>
  </footer>

</div>
</body>
</html>
```